New PowerPoint Design Project

A well-known speaker needs a visual presence that compliments his amazing, consistent performance onstage. You'll easily improve this deck, and I'll leave it to you whether you stick with the palette defined by the original BLQEMS icons you'll find in the deck, the mishmosh in the deck as it stands, OR get extra points by going with the corporate color palette so our speaking slides fit with Ronan's brands and his three sub-brands. A look at the Ronan subbrand .png in the attached zip file might give you some ideas.
Updates

Just noting that I'm available to answer questions or supply assets you think you'd need. The big design issue I'm looking for someone to solve is how you'll treat the bright clusters of icons in information graphics of the deck.

Target Market(s)

Corporate Executives and wanabees

Requirements
Must have
• The footer needs to have the Dellwyn Bluepath logo and Twitter and Facebook link and you need to do the first 27 slides. The slides past 27 are there simply if you want to use assets from those slides.
Nice to have
• Use the palette document in the zip rather than palette dictated by the BLQEMS icons in the deck (I do not have source for the icons.).

```html
<!DOCTYPE html>
<html lang="en">
<head>
<meta charset="utf-8">
<title>Ignition Requires an Empathetic Challenge</title>
<link rel="stylesheet" href="https://fonts.googleapis.com/css2?family=Oswald:wght@300;400&family=Open+Sans:wght@600&display=swap">
<style>
  :root {
    --ink: #111111;
    --lime: #8dc63f;
    --lime-text: #8dc63f;
    --white: #ffffff;
    --sun: #f6c51b;
    --teal: #1bb5c3;
    --ocean: #1a6ea5;
    --crimson: #e5262b;
    --footer-ink: #111111;
  }
  * { margin: 0; padding: 0; box-sizing: border-box; }
  html, body { width: 1200px; height: 674px; overflow: hidden; background: var(--ink); }
  .slide { position: relative; width: 1200px; height: 674px; overflow: hidden; background: var(--lime); }
  .title-panel { position: absolute; left: 0; top: 0; width: 380px; height: 674px; background: var(--ink); }
  .slide-title {
    position: absolute; left: 24px; top: 204px;
    font-family: "Oswald", "Arial Narrow", sans-serif; font-weight: 300;
    font-size: 45px; line-height: 56px; letter-spacing: 1px;
    color: var(--lime-text); text-transform: uppercase;
  }
  .advance-mark { position: absolute; left: 322px; top: 254px; width: 120px; height: 120px; }
  .principle-icon {
    position: absolute; width: 132px; height: 132px; border-radius: 50%;
  }
  .icon-compass { left: 580px; top: 66px; background: var(--sun); }
  .icon-smile { left: 900px; top: 66px; background: var(--teal); }
  .icon-elephant { left: 566px; top: 348px; background: var(--ocean); }
  .icon-heart { left: 878px; top: 348px; background: var(--crimson); display: flex; align-items: center; justify-content: center; }
  .principle-text {
    position: absolute; width: 320px; text-align: center;
    font-family: "Open Sans", Arial, sans-serif; font-weight: 600;
    font-size: 21px; line-height: 28px; color: var(--white);
  }
  .text-judge { left: 486px; top: 204px; }
  .text-levity { left: 806px; top: 210px; }
  .text-elephant { left: 472px; top: 488px; }
  .text-empathy { left: 784px; top: 495px; }
  .brand { position: absolute; left: 16px; top: 644px; display: flex; align-items: center; gap: 10px; }
  .brand-square { width: 22px; height: 22px; background: var(--white); }
  .brand-name {
    font-family: "Open Sans", Arial, sans-serif; font-weight: 600;
    font-size: 21px; color: var(--white); letter-spacing: 0.3px;
  }
  .footer-item {
    position: absolute; top: 646px;
    font-family: "Open Sans", Arial, sans-serif; font-weight: 600;
    font-size: 15px; color: var(--footer-ink);
  }
  .copyright { left: 415px; }
  .social-handle { left: 708px; }
  .social-page { left: 1005px; }
</style>
</head>
<body>
<main class="slide">
  <section class="title-panel">
    <h1 class="slide-title">Ignition<br>requires an<br>empathetic<br>challenge</h1>
  </section>

  <svg class="advance-mark" viewBox="0 0 120 120" aria-hidden="true">
    <circle cx="60" cy="60" r="57" fill="#111111" stroke="#8dc63f" stroke-width="2"/>
    <polygon points="30,40 48,40 66,60 48,80 30,80 48,60" fill="#8dc63f"/>
    <polygon points="54,40 72,40 90,60 72,80 54,80 72,60" fill="#8dc63f"/>
  </svg>

  <div class="principle-icon icon-compass" role="img" aria-label="Drafting compass icon on a yellow circle"></div>
  <p class="principle-text text-judge">Don’t shame or<br>judge where<br>you are</p>

  <div class="principle-icon icon-smile" role="img" aria-label="Smiling icon on a teal circle"></div>
  <p class="principle-text text-levity">Use levity.<br>Create<br>some fun.</p>

  <div class="principle-icon icon-elephant" role="img" aria-label="Pink elephant icon on a blue circle"></div>
  <p class="principle-text text-elephant">Reveal a pink elephant<br>and do so without angst,<br>it’s just the way it is.</p>

  <div class="principle-icon icon-heart">
    <svg width="70" height="62" viewBox="0 0 70 62" aria-hidden="true">
      <path d="M35 60 C12 42 2 30 2 18 C2 8 10 1 19 1 C26 1 32 5 35 11 C38 5 44 1 51 1 C60 1 68 8 68 18 C68 30 58 42 35 60 Z" fill="#ffffff"/>
    </svg>
  </div>
  <p class="principle-text text-empathy">Be empathetic<br>(human<br>/vulnerable)</p>

  <footer>
    <div class="brand">
      <span class="brand-square"></span>
      <span class="brand-name">Dellwyn Bluepath</span>
    </div>
    <span class="footer-item copyright">COPYRIGHT 2013</span>
    <span class="footer-item social-handle">@dellwyn</span>
    <span class="footer-item social-page">/Ronandellwyn</span>
  </footer>
</main>
</body>
</html>
```